Business Card Design for a Sound engineer and DJ

We would like a residn of the business card.

Logo must remain the same.
The card is for the owner of the company.
The business card is in Arabic as the company is based in Kuwait.
The company specializes in sound engineering for singers concerts and events and in addition DJ.
The color options is up to the designer but we would like it masculine as the owner is a man.

Target Market(s)

All ages

Industry/Entity Type

Media

Contact Information for Business Card

Name:
Eng. Tarek Halabi
م/طارق حلبي

The name above is in Arabic and English.

Title: General Manager
Mobile: +965 66307852
Office: +965 22486037
Email: info@sawtarin.net

Address:
Office no. 3
1st floor
Almarfa Complex
Rashed AlQeblawi St.
Salmiya
Kuwait

Instagram: @sawtarin
Snap: sawtarin

Requirements
Nice to have
• can we have Instagram icon and snap icon and a phone vector and email?
• Instead of writing the words

```html
<!DOCTYPE html>
<html lang="en">
<head>
<meta charset="utf-8">
<title>Sawtarin – Business Card</title>
<link rel="stylesheet" href="https://fonts.googleapis.com/css2?family=Cairo:wght@600;700&family=Dosis:wght@700&family=Orbitron:wght@600&family=Roboto:wght@400;500&display=swap">
<style>
  :root {
    --page-bg: #d9d4cc;
    --card-top: #f4f2f0;
    --card-bottom: #e8e3e6;
    --brand-purple: #5e2a73;
    --name-purple: #562c80;
    --title-blue: #4d4f8f;
    --contact-purple: #5a3f8e;
    --icon-fill: #6b6fa6;
    --band-purple: #7a5088;
  }
  * { margin: 0; padding: 0; box-sizing: border-box; }
  html, body { width: 970px; height: 1200px; overflow: hidden; }
  body {
    background: var(--page-bg);
    position: relative;
    font-family: "Roboto", Arial, sans-serif;
  }
  .card {
    position: absolute;
    left: 185px; top: 75px;
    width: 600px; height: 1050px;
    background: linear-gradient(170deg, var(--card-top) 0%, #f7f5f3 55%, var(--card-bottom) 100%);
    box-shadow: 0 10px 30px rgba(0,0,0,0.18);
    overflow: hidden;
  }
  .brand-mark {
    position: absolute; left: 0; right: 0; top: 150px;
    text-align: center;
    font-family: "Cairo", sans-serif;
    font-weight: 700;
    font-size: 150px;
    line-height: 1;
    color: var(--brand-purple);
  }
  .brand-name {
    position: absolute; left: 0; right: 0; top: 400px;
    text-align: center;
    font-family: "Orbitron", sans-serif;
    font-weight: 600;
    font-size: 38px;
    letter-spacing: 12px;
    padding-left: 12px;
    color: var(--brand-purple);
  }
  .services-en {
    position: absolute; left: 0; right: 0; top: 442px;
    text-align: center;
    font-family: "Dosis", sans-serif;
    font-weight: 700;
    font-size: 21px;
    letter-spacing: 2.5px;
    color: var(--brand-purple);
  }
  .services-ar {
    position: absolute; left: 0; right: 0; top: 466px;
    text-align: center;
    font-family: "Cairo", sans-serif;
    font-weight: 600;
    font-size: 22px;
    color: var(--brand-purple);
    direction: rtl;
  }
  .person-name {
    position: absolute; left: 0; right: 0; top: 588px;
    text-align: center;
    font-weight: 500;
    font-size: 35px;
    color: var(--name-purple);
  }
  .person-name-ar {
    position: absolute; left: 0; right: 0; top: 628px;
    text-align: center;
    font-family: "Cairo", sans-serif;
    font-weight: 700;
    font-size: 24px;
    color: var(--name-purple);
    direction: rtl;
  }
  .person-title {
    position: absolute; left: 0; right: 0; top: 670px;
    text-align: center;
    font-size: 25px;
    color: var(--title-blue);
  }
  .contact-list {
    position: absolute; left: 0; right: 0; top: 752px;
    list-style: none;
    display: flex; flex-direction: column; align-items: center;
    gap: 3px;
  }
  .contact-item {
    display: flex; align-items: center; gap: 8px;
    font-size: 27px;
    line-height: 30px;
    color: var(--contact-purple);
  }
  .contact-icon { width: 26px; height: 26px; flex: none; }
  .social-row {
    position: absolute; left: 0; right: 0; top: 862px;
    display: flex; justify-content: center; gap: 22px;
  }
  .social-item {
    display: flex; align-items: center; gap: 8px;
    font-size: 27px;
    color: var(--contact-purple);
  }
  .social-square {
    width: 26px; height: 26px;
    background: var(--icon-fill);
    border-radius: 3px;
  }
  .footer-band {
    position: absolute; left: 0; right: 0; bottom: 0;
    height: 80px;
    background: var(--band-purple);
  }
</style>
</head>
<body>
  <main class="card">
    <div class="brand-mark" dir="rtl">صوترين</div>
    <div class="brand-name">SAWTARIN</div>
    <div class="services-en">DJ - SOUND ENG. - LIGHTING</div>
    <div class="services-ar">دي جي - هندسة صوت - إضاءة</div>

    <h1 class="person-name">Eng. Tarek Halabi</h1>
    <div class="person-name-ar">م/طارق حلبي</div>
    <div class="person-title">General Manager</div>

    <ul class="contact-list">
      <li class="contact-item">
        <svg class="contact-icon" viewBox="0 0 26 26" aria-hidden="true">
          <rect width="26" height="26" rx="3" fill="#6b6fa6"/>
          <rect x="8" y="4" width="10" height="18" rx="2" fill="none" stroke="#fff" stroke-width="1.8"/>
          <rect x="10" y="7" width="6" height="5" fill="#fff"/>
          <circle cx="13" cy="18" r="1.3" fill="#fff"/>
        </svg>
        <span>+965 66307852</span>
      </li>
      <li class="contact-item">
        <svg class="contact-icon" viewBox="0 0 26 26" aria-hidden="true">
          <rect width="26" height="26" rx="3" fill="#6b6fa6"/>
          <path d="M5 10 Q13 4 21 10 L19 12 L16 10 L10 10 L7 12 Z" fill="#fff"/>
          <rect x="8" y="12" width="10" height="8" rx="1.5" fill="#fff"/>
        </svg>
        <span>+965 22486037</span>
      </li>
      <li class="contact-item">
        <svg class="contact-icon" viewBox="0 0 26 26" aria-hidden="true">
          <rect width="26" height="26" rx="3" fill="#6b6fa6"/>
          <rect x="4" y="7" width="18" height="12" fill="#fff"/>
          <path d="M4 7 L13 14 L22 7" fill="none" stroke="#6b6fa6" stroke-width="1.5"/>
        </svg>
        <span>info@sawtarin.net</span>
      </li>
    </ul>

    <div class="social-row">
      <div class="social-item"><span class="social-square"></span><span>@sawtarin</span></div>
      <div class="social-item"><span class="social-square"></span><span>@sawtarin</span></div>
    </div>

    <div class="footer-band"></div>
  </main>
</body>
</html>
```